Grand Chart of Bold Reformers

Hi - I would like your help transforming my (terrible) drawing into a graphic that pops -using hex colors I'll give you - so that I can put it into stationary and on t-shirts or tote bags. My company, the Marrowgate Institute, trains social change leaders (from the sectors in the periodic table) on how to lead large-scale change. I have this vision - the "periodic table" but these are the sectors that my clients work in. If you are having trouble reading my writing, I apologize. Our hex colors are: #114769, #76984C, #80B5CF (Seagull), #8F2C63 and Rangoon Black #191919. You don't need to use all of them, but it'd be good to be consistent with our overall branding. If you can't read my writing, I will send correct spelling. The "Marrowgate" with the flowers on the bottom is for a separate design bid.

Target Market(s)

nonprofit, social entrepreneurs, philanthropy, leaders

Requirements
Must have
• clean, readable font. alignment to look like periodic table of elements. heart icon for love, cat face for cats.

```html
<!DOCTYPE html>
<html lang="en">
<head>
<meta charset="utf-8">
<title>Grand Chart of Bold Reformers</title>
<link rel="stylesheet" href="https://fonts.googleapis.com/css2?family=Oswald:wght@400&display=swap">
<style>
  :root {
    --navy: #114769;
    --ink: #191919;
    --white: #ffffff;

    --c-anti: #114769;
    --c-belong: #22889f;

    --g1: #76984c; --g2: #7e9c50; --g3: #86a656; --g4: #8dac5a; --g5: #95b25f; --g6: #a0bb66;
    --b1: #80b5cf; --b2: #71adc5; --b3: #5ea6be; --b4: #489db3; --b5: #2f98a4; --b6: #14878c;
    --m1: #8f2c63; --m2: #9d2f6e; --m3: #a83478; --m4: #b03c88; --m5: #bd4699; --m6: #c94fb1;
    --v1: #114769; --v2: #164f73; --v3: #1b6382; --v4: #1d7290; --v5: #2488a1;

    --cell-w: 129.5px;
    --cell-h: 92px;
  }
  * { box-sizing: border-box; margin: 0; padding: 0; }
  html, body { width: 1200px; height: 1109px; overflow: hidden; background: var(--white); }
  body { position: relative; font-family: "Oswald", sans-serif; font-weight: 400; color: var(--white); }

  .chart { position: absolute; left: 211px; top: 123px; width: 777px; height: 368px; }
  .cell {
    position: absolute; width: var(--cell-w); height: var(--cell-h);
    text-align: center; font-size: 21px; line-height: 22px; padding-top: 13px; padding-left: 4px;
  }
  .cell.single { padding-top: 21px; }
  .cell .icon { position: absolute; left: 8px; bottom: 8px; width: 26px; height: 26px; }

  .values { position: absolute; left: 211px; top: 537.5px; width: 777.5px; height: 92px; display: flex; }
  .value { position: relative; flex: 1; text-align: center; font-size: 21px; line-height: 22px; padding-top: 20px; padding-left: 12px; }
  .value .icon { position: absolute; left: 8px; bottom: 10px; width: 28px; height: 28px; }

  .wordmark {
    position: absolute; left: 0; width: 1200px; top: 850px; text-align: center;
    color: var(--navy); font-weight: 400; font-size: 110px; line-height: 130px;
  }
</style>
</head>
<body>

<svg width="0" height="0" style="position:absolute" aria-hidden="true">
  <defs>
    <symbol id="i-heart" viewBox="0 0 24 24"><path fill="currentColor" d="M12 21 3.5 12.6A5 5 0 0 1 12 5.5a5 5 0 0 1 8.5 7.1z"/></symbol>
    <symbol id="i-cat" viewBox="0 0 24 24"><path fill="currentColor" d="M3 3l5 4.5h8L21 3v11c0 4.5-4 7.5-9 7.5S3 18.5 3 14z"/><circle cx="9" cy="13" r="1.2" fill="var(--m2)"/><circle cx="15" cy="13" r="1.2" fill="var(--m2)"/><path d="M11 16h2l-1 1z" fill="var(--m2)"/></symbol>
    <symbol id="i-house" viewBox="0 0 24 24"><path fill="currentColor" d="M12 3 2 12h3v9h5v-6h4v6h5v-9h3z"/></symbol>
    <symbol id="i-book" viewBox="0 0 24 24"><path fill="none" stroke="currentColor" stroke-width="1.6" d="M2 5c4-1 7 0 10 2 3-2 6-3 10-2v14c-4-1-7 0-10 2-3-2-6-3-10-2zM12 7v14"/></symbol>
    <symbol id="i-search" viewBox="0 0 24 24"><circle cx="9" cy="9" r="6.5" fill="none" stroke="currentColor" stroke-width="2.5"/><path d="M14 14l7 7" stroke="currentColor" stroke-width="3.5" stroke-linecap="round"/></symbol>
    <symbol id="i-scale" viewBox="0 0 24 24"><path fill="none" stroke="currentColor" stroke-width="1.6" d="M12 3v18M7 21h10M4 6h16M4 6l-3 7h6zM20 6l-3 7h6z"/><path fill="currentColor" d="M1 13h6a3 3 0 0 1-6 0zM17 13h6a3 3 0 0 1-6 0z"/></symbol>
    <symbol id="i-shield" viewBox="0 0 24 24"><path fill="currentColor" d="M12 2 4 5v6c0 5 3.5 9 8 11 4.5-2 8-6 8-11V5z"/><path d="M8 12l3 3 5-6" fill="none" stroke="var(--v2)" stroke-width="2.2"/></symbol>
    <symbol id="i-people" viewBox="0 0 24 24"><circle cx="6" cy="8" r="2.5" fill="currentColor"/><circle cx="18" cy="8" r="2.5" fill="currentColor"/><circle cx="12" cy="5" r="2.5" fill="currentColor"/><rect x="3" y="11" width="6" height="10" rx="2" fill="currentColor"/><rect x="15" y="11" width="6" height="10" rx="2" fill="currentColor"/><rect x="9.5" y="8" width="5" height="8" rx="2" fill="currentColor"/></symbol>
    <symbol id="i-dot" viewBox="0 0 24 24"><circle cx="12" cy="12" r="9" fill="currentColor"/></symbol>
    <symbol id="i-globe" viewBox="0 0 24 24"><circle cx="12" cy="12" r="9" fill="none" stroke="currentColor" stroke-width="1.8"/><path d="M3 12h18M12 3c3 3 3 15 0 18M12 3c-3 3-3 15 0 18" fill="none" stroke="currentColor" stroke-width="1.4"/></symbol>
    <symbol id="i-leaf" viewBox="0 0 24 24"><path fill="currentColor" d="M21 3C10 3 6 8 7 16c8 1 14-3 14-13z"/><path d="M4 22c2-5 6-9 10-12" stroke="currentColor" stroke-width="1.6" fill="none"/></symbol>
    <symbol id="i-gear" viewBox="0 0 24 24"><circle cx="12" cy="12" r="7" fill="none" stroke="currentColor" stroke-width="4" stroke-dasharray="3 2"/><circle cx="12" cy="12" r="5" fill="none" stroke="currentColor" stroke-width="2"/></symbol>
    <symbol id="i-hands" viewBox="0 0 24 24"><path fill="currentColor" d="M10 21 4 14V6l2 1v5l4 3zM14 21l6-7V6l-2 1v5l-4 3z"/></symbol>
    <symbol id="i-school" viewBox="0 0 24 24"><path fill="currentColor" d="M12 2v3l-5 4v3H3v10h18V12h-4V9l-5-4z"/><rect x="10.5" y="16" width="3" height="6" fill="var(--b2)"/></symbol>
  </defs>
</svg>

<main class="chart" aria-label="Grand Chart of Bold Reformers">
  <div class="cell" style="left:0;top:0;background:var(--c-anti)">Anti<br>Violence<svg class="icon"><use href="#i-heart"/></svg></div>
  <div class="cell single" style="left:647.5px;top:0;background:var(--c-belong);padding-top:18px">Belonging<svg class="icon"><use href="#i-people"/></svg></div>

  <div class="cell" style="left:0;top:92px;background:var(--g1)">Early<br>Child<svg class="icon"><use href="#i-dot"/></svg></div>
  <div class="cell" style="left:129.5px;top:92px;background:var(--g2)">Climate<br>Change<svg class="icon"><use href="#i-globe"/></svg></div>
  <div class="cell" style="left:259px;top:92px;background:var(--g3)">Environmental<br>Justice<svg class="icon"><use href="#i-leaf"/></svg></div>
  <div class="cell" style="left:388.5px;top:92px;background:var(--g4)">Human<br>Service<svg class="icon"><use href="#i-gear"/></svg></div>
  <div class="cell" style="left:518px;top:92px;background:var(--g5)">Health<br>Care<svg class="icon"><use href="#i-heart"/></svg></div>
  <div class="cell single" style="left:647.5px;top:92px;background:var(--g6)">Housing<svg class="icon"><use href="#i-house"/></svg></div>

  <div class="cell single" style="left:0;top:184px;background:var(--b1)">Education<svg class="icon"><use href="#i-book"/></svg></div>
  <div class="cell" style="left:129.5px;top:184px;background:var(--b2)">Alter<br>School<svg class="icon"><use href="#i-school"/></svg></div>
  <div class="cell" style="left:259px;top:184px;background:var(--b3)">Social<br>Justice<svg class="icon"><use href="#i-scale"/></svg></div>
  <div class="cell" style="left:388.5px;top:184px;background:var(--b4)">Civil<br>Rights<svg class="icon"><use href="#i-gear"/></svg></div>
  <div class="cell" style="left:518px;top:184px;background:var(--b5)">Health<br>Equity<svg class="icon"><use href="#i-heart"/></svg></div>
  <div class="cell" style="left:647.5px;top:184px;background:var(--b6)">Jobs<svg class="icon"><use href="#i-search"/></svg></div>

  <div class="cell" style="left:0;top:276px;background:var(--m1)">Animal<br>Welfare<svg class="icon"><use href="#i-dot"/></svg></div>
  <div class="cell" style="left:129.5px;top:276px;background:var(--m2)">Cats<svg class="icon"><use href="#i-cat"/></svg></div>
  <div class="cell" style="left:259px;top:276px;background:var(--m3)">Racial<br>Justice<svg class="icon"><use href="#i-dot"/></svg></div>
  <div class="cell" style="left:388.5px;top:276px;background:var(--m4)">Immigration<br>Right<svg class="icon"><use href="#i-globe"/></svg></div>
  <div class="cell" style="left:518px;top:276px;background:var(--m5)">Behavior<br>Wealth<svg class="icon"><use href="#i-gear"/></svg></div>
  <div class="cell" style="left:647.5px;top:276px;background:var(--m6)">Inter<br>Generational<svg class="icon"><use href="#i-people"/></svg></div>
</main>

<section class="values" aria-label="Values">
  <div class="value" style="background:var(--v1)">Love<svg class="icon"><use href="#i-heart"/></svg></div>
  <div class="value" style="background:var(--v2)">Authencity<svg class="icon"><use href="#i-shield"/></svg></div>
  <div class="value" style="background:var(--v3)">Humility<svg class="icon"><use href="#i-hands"/></svg></div>
  <div class="value" style="background:var(--v4)">Audacity<svg class="icon"><use href="#i-hands"/></svg></div>
  <div class="value" style="background:var(--v5)">Justice<svg class="icon"><use href="#i-scale"/></svg></div>
</section>

<div class="wordmark">Marrowgate</div>

</body>
</html>
```